Search Fund needs a PowerPoint template design

We need a eye-catching and compelling PowerPoint design for a new company based in Chicago called Tarn Ridge Partners. We are search fund with a primary mission to acquire a founder/family/entrepreneur owned businesses (This is similar to a Private Equity firm). Our goal is to offer investors a unique avenue to invest in an attractive business acquisition while providing business owners with an alternative path to exit. We would like the design to reflect crisp and professional nature that many financial firms present. The template should build on the design of the logo including expanding a logical color palette. The presentation will be used to describe facts regarding the firm, financial data and key messaging that we want our investors and potential partners to takeaway.

Target Market(s)

Financial Investors

Industry/Entity Type

Finance

Font styles to use
Serif
Sans Serif

Colors

Designer to choose colors to be used in the design.

Requirements
Must have
• Should include cover page and slide examples. Attractive data displays (graphs, charts, infographics etc.); Compelling cover; fly pages to put in between sections; table of contents page. Needs to have white space to add text.
Should not have
• Do not redesign the logo or change the logo colors. Additional colors should be added to the PowerPoint template

```html
<!DOCTYPE html>
<html lang="en">
<head>
<meta charset="utf-8">
<title>Tarn Ridge Partners – Presentation Template</title>
<link href="https://fonts.googleapis.com/css2?family=Open+Sans:wght@300;400;600;700&display=swap" rel="stylesheet">
<style>
:root{
  --page:#e9e8e6;
  --white:#ffffff;
  --blue:#1e9be9;
  --blue-mid:#4aa8e6;
  --blue-light:#8cc7f0;
  --navy:#1466c0;
  --ink:#333333;
  --muted:#7a7a7a;
  --rule:#e3e6ea;
  --track:#e4e4e4;
}
*{margin:0;padding:0;box-sizing:border-box}
html,body{width:810px;height:1200px;overflow:hidden;background:var(--page);font-family:"Open Sans",Arial,sans-serif;color:var(--ink)}
.deck{position:absolute;left:6px;top:74px;display:grid;grid-template-columns:repeat(3,258px);grid-auto-rows:144px;column-gap:10px;row-gap:10.5px}
.slide{position:relative;background:var(--white);overflow:hidden}
.abs{position:absolute}
.title{position:absolute;font-weight:300;font-size:11.5px;line-height:1.25;color:var(--ink)}
.title.center{left:0;right:0;text-align:center}
.kicker{position:absolute;font-size:2.4px;color:var(--muted);letter-spacing:.2px;text-transform:uppercase}
.lbl{font-size:3.8px;color:var(--blue);line-height:1.3;margin-bottom:1.5px}
.body{font-size:3.1px;line-height:1.55;color:#666}
.item{position:absolute;width:62px}
.item .row{display:flex;align-items:center;gap:2.5px}
.foot{position:absolute;left:10px;bottom:5px;font-size:3.8px;font-weight:700;color:var(--navy);letter-spacing:.2px}
.pg{position:absolute;right:9px;bottom:5px;font-size:2.8px;color:#999}
.photo{position:absolute}
.ico{width:6px;height:6px;flex:none}
.dot{width:5px;height:5px;border-radius:50%;background:var(--blue);color:#fff;font-size:2.8px;display:flex;align-items:center;justify-content:center;flex:none}
.mark{width:5px;height:5px;border-radius:50%;border:.5px solid var(--blue);color:var(--blue);font-size:3px;display:flex;align-items:center;justify-content:center;flex:none}
.mark.on{background:var(--blue);color:#fff}
/* cover */
.cover-name{position:absolute;top:34px;left:0;right:0;text-align:center;font-size:12px;font-weight:700;color:var(--navy);letter-spacing:.6px}
.cover-title{position:absolute;top:96px;left:0;right:0;text-align:center;font-size:17px;font-weight:400;color:#fff;letter-spacing:.8px}
/* tiles */
.tile{position:absolute;top:46px;width:68px;height:68px;padding:8px 6px;text-align:center;color:#fff}
.tile .lbl,.tile .body{color:#fff}
.tile svg{display:block;margin:0 auto 10px}
.stat{position:absolute;top:18px;width:68px;height:110px;border:.6px solid #b9dcf5;text-align:center;padding:10px 5px}
.stat .num{font-size:11px;font-weight:300;color:var(--blue);margin-bottom:8px}
.pill{position:absolute;height:4px;border-radius:2px;border:.4px solid var(--blue);font-size:1.8px;color:var(--blue);display:flex;align-items:center;justify-content:center}
.pill.fill{background:var(--blue);color:#fff}
.year-row{position:absolute;left:18px;right:18px;height:24px;border-bottom:.5px solid var(--rule)}
.year-row .yr{position:absolute;left:2px;top:2px;font-size:4px;color:var(--blue)}
.year-row .yt{position:absolute;left:28px;top:2px;font-size:3.8px;line-height:1.3;color:var(--blue);width:50px}
.year-row .body{position:absolute;left:102px;top:2px;width:120px}
.bignum{position:absolute;top:93px;width:40px;text-align:center;font-size:11px;font-weight:300;color:var(--blue)}
.bignum span{display:block;font-size:2.4px;color:#555}
.chip{position:absolute;top:90px;width:37px;height:20px;background:var(--blue);padding:2px 3px}
.chip .lbl,.chip .body{color:#fff;font-size:2.4px}
.bar-lbl{position:absolute;font-size:2.4px;color:#555;width:82px;display:flex;justify-content:space-between}
.bar{position:absolute;height:1.6px;background:var(--blue)}
.step{position:absolute;width:40px}
.tag{display:inline-block;background:var(--blue);color:#fff;font-size:2px;padding:.6px 3px;margin-bottom:2px}
</style>
</head>
<body>
<main class="deck">

  <!-- 1 Cover -->
  <section class="slide">
    <div class="cover-name">TARN RIDGE PARTNERS</div>
    <svg class="abs" style="left:0;top:0" width="258" height="144" viewBox="0 0 258 144">
      <defs><linearGradient id="coverBand" x1="0" y1="0" x2="1" y2="1"><stop offset="0" stop-color="#2bb5f2"/><stop offset="1" stop-color="#1270c8"/></linearGradient></defs>
      <path d="M0,98 Q129,42 258,98 V144 H0Z" fill="url(#coverBand)"/>
    </svg>
    <div class="cover-title">MAIN&nbsp; TITLE HERE</div>
  </section>

  <!-- 2 Agenda -->
  <section class="slide">
    <div class="kicker" style="left:20px;top:14px">Subtitle text</div>
    <div class="title" style="left:20px;top:19px">Presentation<br>Agenda</div>
    <div class="item" style="left:150px;top:18px;width:90px"><div class="lbl">01. Text about service</div><p class="body">Short note on this agenda point, kept brief and clear so readers follow it.</p></div>
    <div class="item" style="left:150px;top:48px;width:90px"><div class="lbl">02. Text about service</div><p class="body">Short note on this agenda point, kept brief and clear so readers follow it.</p></div>
    <div class="item" style="left:150px;top:78px;width:90px"><div class="lbl">03. Text about service</div><p class="body">Short note on this agenda point, kept brief and clear so readers follow it.</p></div>
    <div class="item" style="left:150px;top:108px;width:90px"><div class="lbl">04. Text about service</div><p class="body">Short note on this agenda point, kept brief and clear so readers follow it.</p></div>
  </section>

  <!-- 3 Services -->
  <section class="slide">
    <div class="title" style="left:18px;top:16px">Our Services</div>
    <div class="item" style="left:20px;top:44px"><div class="row"><svg class="ico" viewBox="0 0 6 6"><path d="M1 1h4v2L3 5 1 3z" fill="none" stroke="#1e9be9" stroke-width=".5"/></svg><div class="lbl">Text about service</div></div><p class="body">Brief line about this service<br>and the value it brings to<br>owners and investors.</p></div>
    <div class="item" style="left:98px;top:44px"><div class="row"><svg class="ico" viewBox="0 0 6 6"><path d="M1 2l2-1 2 1-2 3z" fill="none" stroke="#1e9be9" stroke-width=".5"/></svg><div class="lbl">Text about service</div></div><p class="body">Brief line about this service<br>and the value it brings to<br>owners and investors.</p></div>
    <div class="item" style="left:176px;top:44px"><div class="row"><svg class="ico" viewBox="0 0 6 6"><path d="M1 5l4-4M3 1h2v2" fill="none" stroke="#1e9be9" stroke-width=".5"/></svg><div class="lbl">Text about service</div></div><p class="body">Brief line about this service<br>and the value it brings to<br>owners and investors.</p></div>
    <div class="item" style="left:20px;top:81px"><div class="row"><svg class="ico" viewBox="0 0 6 6"><rect x="1" y="1.5" width="4" height="3.5" fill="none" stroke="#1e9be9" stroke-width=".5"/></svg><div class="lbl">Text about service</div></div><p class="body">Brief line about this service<br>and the value it brings to<br>owners and investors.</p></div>
    <div class="item" style="left:98px;top:81px"><div class="row"><svg class="ico" viewBox="0 0 6 6"><path d="M1 3l2 2 2-4" fill="none" stroke="#1e9be9" stroke-width=".5"/></svg><div class="lbl">Text about service</div></div><p class="body">Brief line about this service<br>and the value it brings to<br>owners and investors.</p></div>
    <div class="item" style="left:176px;top:81px"><div class="row"><svg class="ico" viewBox="0 0 6 6"><rect x="1" y="1" width="4" height="4" rx="1" fill="none" stroke="#1e9be9" stroke-width=".5"/></svg><div class="lbl">Text about service</div></div><p class="body">Brief line about this service<br>and the value it brings to<br>owners and investors.</p></div>
    <div class="foot">Tarn Ridge Partners</div><div class="pg">4</div>
  </section>

  <!-- 4 Photo & text -->
  <section class="slide">
    <div class="title" style="left:20px;top:27px">Demo slide<br>Photo <span style="display:inline-block;width:11px;height:11px;border-radius:50%;background:var(--blue-light);color:#fff;font-size:7px;text-align:center;line-height:11px">&amp;</span> text block</div>
    <div class="item" style="left:20px;top:86px"><div class="lbl">Text about service</div><p class="body">Brief line about this topic<br>and what it means for our<br>partners over time.</p></div>
    <div class="item" style="left:100px;top:86px"><div class="lbl">Text about service</div><p class="body">Brief line about this topic<br>and what it means for our<br>partners over time.</p></div>
    <div class="item" style="left:180px;top:86px"><div class="lbl">Text about service</div><p class="body">Brief line about this topic<br>and what it means for our<br>partners over time.</p></div>
    <div class="foot">Tarn Ridge Partners</div><div class="pg">6</div>
  </section>

  <!-- 5 Infographic -->
  <section class="slide">
    <div class="title center" style="top:11px">Demo slide<br>Infographic block</div>
    <div class="tile" style="left:20px;background:#1ea0ea"><svg width="10" height="9" viewBox="0 0 10 9"><rect x="1" y="1" width="8" height="6" fill="none" stroke="#fff" stroke-width=".6"/><path d="M3 5l2-2 2 1" fill="none" stroke="#fff" stroke-width=".6"/></svg><div class="lbl">Text about service</div><p class="body">Brief line about this block<br>with a short supporting<br>point for readers.</p></div>
    <div class="tile" style="left:95px;background:var(--blue-mid)"><svg width="10" height="9" viewBox="0 0 10 9"><rect x="1" y="2.5" width="8" height="5.5" fill="none" stroke="#fff" stroke-width=".6"/><path d="M3.5 2.5V1h3v1.5" fill="none" stroke="#fff" stroke-width=".6"/></svg><div class="lbl">Text about service</div><p class="body">Brief line about this block<br>with a short supporting<br>point for readers.</p></div>
    <div class="tile" style="left:170px;background:var(--blue-light)"><svg width="10" height="9" viewBox="0 0 10 9"><path d="M1 8h8M2 8V6M4 8V4M6 8V5M8 8V2" fill="none" stroke="#fff" stroke-width=".6"/></svg><div class="lbl">Text about service</div><p class="body">Brief line about this block<br>with a short supporting<br>point for readers.</p></div>
    <div class="foot">Tarn Ridge Partners</div><div class="pg">7</div>
  </section>

  <!-- 6 Banner photo -->
  <section class="slide">
    <div class="photo" role="img" aria-label="Wide landscape photo of a hilltop castle above a valley" style="left:20px;top:18px;width:219px;height:48px;background:linear-gradient(180deg,#8fb6d8 0%,#c9d3d9 45%,#6f8a5a 75%,#3f6a34 100%)"></div>
    <div class="item" style="left:20px;top:83px"><div class="row"><svg class="ico" viewBox="0 0 6 6"><path d="M1 1h4v2L3 5 1 3z" fill="none" stroke="#1e9be9" stroke-width=".5"/></svg><div class="lbl">Text about service</div></div><p class="body">Brief line about this service<br>and the value it brings to<br>owners and investors.</p></div>
    <div class="item" style="left:98px;top:83px"><div class="row"><svg class="ico" viewBox="0 0 6 6"><path d="M1 2l2-1 2 1-2 3z" fill="none" stroke="#1e9be9" stroke-width=".5"/></svg><div class="lbl">Text about service</div></div><p class="body">Brief line about this service<br>and the value it brings to<br>owners and investors.</p></div>
    <div class="item" style="left:176px;top:83px"><div class="row"><svg class="ico" viewBox="0 0 6 6"><path d="M1 5l4-4M3 1h2v2" fill="none" stroke="#1e9be9" stroke-width=".5"/></svg><div class="lbl">Text about service</div></div><p class="body">Brief line about this service<br>and the value it brings to<br>owners and investors.</p></div>
    <div class="foot">Tarn Ridge Partners</div><div class="pg">8</div>
  </section>

  <!-- 7 Company info over photo -->
  <section class="slide">
    <div class="photo" role="img" aria-label="Photo of a waterfall over green cliffs under a pastel sky" style="inset:0;background:linear-gradient(180deg,#e7c9d6 0%,#d9dbe6 30%,#b9cf9c 60%,#8eb26a 100%)"></div>
    <div class="abs" style="inset:0;background:rgba(255,255,255,.45)"></div>
    <div class="title center" style="top:46px;font-size:11px">Information about<br>Our Company</div>
    <p class="body abs" style="top:78px;left:0;right:0;text-align:center;color:#444">Short line that sums up who we are and what we do.</p>
    <div class="bignum" style="left:65px">98<span>Lorem ipsum dolor</span></div>
    <div class="bignum" style="left:107px">81<span>Lorem ipsum dolor</span></div>
    <div class="bignum" style="left:148px">35<span>Lorem ipsum dolor</span></div>
    <div class="bignum" style="left:189px">40<span>Lorem ipsum dolor</span></div>
  </section>

  <!-- 8 Yearly planning -->
  <section class="slide">
    <div class="title" style="left:18px;top:14px">Yearly Planning</div>
    <div class="abs" style="left:18px;right:18px;top:36px;border-top:.5px solid var(--rule)"></div>
    <div class="year-row" style="top:40px"><div class="yr">2018</div><div class="yt">Title text information about company</div><p class="body">Brief summary of the plan for this year, the key goals we set and how we track progress along the way.</p></div>
    <div class="year-row" style="top:68px"><div class="yr">2019</div><div class="yt">Title text information about company</div><p class="body">Brief summary of the plan for this year, the key goals we set and how we track progress along the way.</p></div>
    <div class="year-row" style="top:96px;border-bottom:none"><div class="yr">2020</div><div class="yt">Title text information about company</div><p class="body">Brief summary of the plan for this year, the key goals we set and how we track progress along the way.</p></div>
    <div class="foot">Tarn Ridge Partners</div><div class="pg">10</div>
  </section>

  <!-- 9 Text with photo right -->
  <section class="slide">
    <div class="title" style="left:18px;top:24px">Demo slide<br>With text</div>
    <p class="body abs" style="left:18px;top:52px;width:100px">A short paragraph about the firm and its approach. We partner with owners who seek a clear path to exit, and we give investors direct access to one well chosen business with steady cash flow and room to grow.</p>
    <div class="pill" style="left:18px;top:107px;width:16px">Learn more</div>
    <div class="pill fill" style="left:38px;top:107px;width:12px">Apply</div>
    <div class="pill" style="left:18px;top:114px;width:10px">Read</div>
    <div class="pill" style="left:31px;top:114px;width:11px">Contact</div>
    <div class="photo" role="img" aria-label="Photo of a waterfall beside green hills at sunset" style="left:130px;top:0;width:128px;height:144px;background:linear-gradient(180deg,#b58fb8 0%,#e5a8a6 28%,#8fb26b 55%,#3f6b2f 85%,#2c4a24 100%)"></div>
    <div class="foot">Tarn Ridge Partners</div>
  </section>

  <!-- 10 Numbered checklist -->
  <section class="slide">
    <div class="title" style="left:18px;top:16px">Numbered Checklist</div>
    <div class="item" style="left:20px;top:44px"><div class="row"><span class="dot">1</span><div class="lbl">Text about service</div></div><p class="body" style="padding-left:7px">Brief line for this step<br>with a short detail that<br>explains the point.</p></div>
    <div class="item" style="left:98px;top:44px"><div class="row"><span class="dot">2</span><div class="lbl">Text about service</div></div><p class="body" style="padding-left:7px">Brief line for this step<br>with a short detail that<br>explains the point.</p></div>
    <div class="item" style="left:176px;top:44px"><div class="row"><span class="dot">3</span><div class="lbl">Text about service</div></div><p class="body" style="padding-left:7px">Brief line for this step<br>with a short detail that<br>explains the point.</p></div>
    <div class="item" style="left:20px;top:81px"><div class="row"><span class="dot">4</span><div class="lbl">Text about service</div></div><p class="body" style="padding-left:7px">Brief line for this step<br>with a short detail that<br>explains the point.</p></div>
    <div class="item" style="left:98px;top:81px"><div class="row"><span class="dot">5</span><div class="lbl">Text about service</div></div><p class="body" style="padding-left:7px">Brief line for this step<br>with a short detail that<br>explains the point.</p></div>
    <div class="item" style="left:176px;top:81px"><div class="row"><span class="dot">6</span><div class="lbl">Text about service</div></div><p class="body" style="padding-left:7px">Brief line for this step<br>with a short detail that<br>explains the point.</p></div>
    <div class="foot">Tarn Ridge Partners</div><div class="pg">11</div>
  </section>

  <!-- 11 Blue card with text -->
  <section class="slide">
    <div class="abs" style="left:24px;top:18px;width:70px;height:92px;background:var(--blue);padding:10px 6px;text-align:center">
      <svg width="10" height="9" viewBox="0 0 10 9" style="display:block;margin:0 auto 10px"><rect x="1" y="1" width="8" height="6" fill="none" stroke="#fff" stroke-width=".6"/><path d="M3 5l2-2 2 1" fill="none" stroke="#fff" stroke-width=".6"/></svg>
      <div class="lbl" style="color:#fff">Text about service</div>
      <p class="body" style="color:#fff">Brief line about this block<br>with a short supporting<br>point for readers.</p>
      <div style="margin:12px auto 0;width:20px;height:3.5px;border-radius:2px;background:#1178cf;font-size:1.8px;color:#fff;line-height:3.5px">Read more</div>
    </div>
    <div class="title" style="left:122px;top:30px">Demo slide<br>With text</div>
    <p class="body abs" style="left:122px;top:64px;width:115px">A short paragraph about the firm and its approach. We partner with owners who seek a clear path to exit, and we give investors direct access to one well chosen business with steady cash flow and room to grow over the long term.</p>
    <div class="foot">Tarn Ridge Partners</div><div class="pg">12</div>
  </section>

  <!-- 12 Checklist -->
  <section class="slide">
    <div class="title" style="left:18px;top:16px">Checklist</div>
    <div class="item" style="left:20px;top:44px"><div class="row"><span class="mark">✕</span><div class="lbl">Text about service</div></div><p class="body" style="padding-left:7px">Brief line for this item<br>with a short detail that<br>explains the point.</p></div>
    <div class="item" style="left:98px;top:44px"><div class="row"><span class="mark">✕</span><div class="lbl">Text about service</div></div><p class="body" style="padding-left:7px">Brief line for this item<br>with a short detail that<br>explains the point.</p></div>
    <div class="item" style="left:176px;top:44px"><div class="row"><span class="mark on">✓</span><div class="lbl">Text about service</div></div><p class="body" style="padding-left:7px">Brief line for this item<br>with a short detail that<br>explains the point.</p></div>
    <div class="item" style="left:20px;top:81px"><div class="row"><span class="mark on">✓</span><div class="lbl">Text about service</div></div><p class="body" style="padding-left:7px">Brief line for this item<br>with a short detail that<br>explains the point.</p></div>
    <div class="item" style="left:98px;top:81px"><div class="row"><span class="mark">✕</span><div class="lbl">Text about service</div></div><p class="body" style="padding-left:7px">Brief line for this item<br>with a short detail that<br>explains the point.</p></div>
    <div class="item" style="left:176px;top:81px"><div class="row"><span class="mark on">✓</span><div class="lbl">Text about service</div></div><p class="body" style="padding-left:7px">Brief line for this item<br>with a short detail that<br>explains the point.</p></div>
    <div class="foot">Tarn Ridge Partners</div><div class="pg">13</div>
  </section>

  <!-- 13 Photo left with text -->
  <section class="slide">
    <div class="photo" role="img" aria-label="Photo of a stone castle on a forested hill" style="left:0;top:0;width:130px;height:144px;background:linear-gradient(180deg,#9fb2c4 0%,#c8ccd0 35%,#8a8f86 55%,#4f7a3a 80%,#35592a 100%)"></div>
    <div class="title" style="left:150px;top:24px">Demo slide<br>With text</div>
    <p class="body abs" style="left:150px;top:56px;width:95px">A short paragraph about the firm and its approach. We partner with owners who want a clear exit and give investors access to a single strong business.</p>
    <p class="body abs" style="left:150px;top:92px;width:95px"><span style="color:var(--blue)">●</span> First point stated in one short line<br><span style="color:var(--blue)">●</span> Second point stated in one short line<br><span style="color:var(--blue)">●</span> Third point stated in one short line</p>
  </section>

  <!-- 14 Stat boxes -->
  <section class="slide">
    <div class="stat" style="left:20px"><div class="num">5,760</div><div class="lbl" style="color:var(--blue-light)">Text about service</div><p class="body">Brief line about this figure<br>and the period it covers<br>for our partners.</p></div>
    <div class="stat" style="left:95px"><div class="num">3,110</div><div class="lbl" style="color:var(--blue-light)">Text about service</div><p class="body">Brief line about this figure<br>and the period it covers<br>for our partners.</p></div>
    <div class="stat" style="left:170px"><div class="num">8,900</div><div class="lbl" style="color:var(--blue-light)">Text about service</div><p class="body">Brief line about this figure<br>and the period it covers<br>for our partners.</p></div>
    <div class="foot">Tarn Ridge Partners</div><div class="pg">16</div>
  </section>

  <!-- 15 Thermometer chart -->
  <section class="slide">
    <svg class="abs" style="left:0;top:0" width="120" height="144" viewBox="0 0 120 144">
      <defs><linearGradient id="thermoFill" x1="0" y1="0" x2="0" y2="1"><stop offset="0" stop-color="#f2d23a"/><stop offset=".45" stop-color="#8cc7f0"/><stop offset="1" stop-color="#1e9be9"/></linearGradient></defs>
      <g font-family="Open Sans,Arial,sans-serif" font-size="3" fill="#444">
        <text x="37" y="27">2017</text><text x="37" y="39">2018</text><text x="37" y="51">2019</text><text x="37" y="63">2020</text><text x="37" y="75">2021</text><text x="37" y="87">2022</text><text x="37" y="99">2023</text>
      </g>
      <rect x="54" y="38" width="24" height="1" fill="#1e9be9"/>
      <rect x="60" y="22" width="12" height="78" rx="6" fill="#f0f0f0"/>
      <rect x="62" y="38" width="8" height="58" fill="url(#thermoFill)"/>
      <circle cx="66" cy="102" r="7" fill="#f0f0f0"/>
      <circle cx="66" cy="102" r="5" fill="#1e9be9"/>
    </svg>
    <div class="title" style="left:122px;top:30px">Demo slide<br>With text</div>
    <p class="body abs" style="left:122px;top:62px;width:115px">A short paragraph about the firm and its approach. We partner with owners who seek a clear path to exit, and we give investors direct access to one well chosen business with steady cash flow and room to grow.</p>
    <div class="foot">Tarn Ridge Partners</div><div class="pg">17</div>
  </section>

  <!-- 16 Concentric circles -->
  <section class="slide">
    <div class="title" style="left:18px;top:28px">Demo slide<br>With text</div>
    <p class="body abs" style="left:18px;top:58px;width:118px">A short paragraph about the firm and its approach. We partner with owners who seek a clear path to exit and give investors access to one well chosen business.</p>
    <div class="chip" style="left:18px"><div class="lbl">Step 01</div><p class="body">Short line for<br>this step here</p></div>
    <div class="chip" style="left:57px"><div class="lbl">Step 02</div><p class="body">Short line for<br>this step here</p></div>
    <div class="chip" style="left:96px"><div class="lbl">Step 03</div><p class="body">Short line for<br>this step here</p></div>
    <svg class="abs" style="left:160px;top:22px" width="72" height="72" viewBox="0 0 72 72">
      <circle cx="36" cy="36" r="34" fill="#1470c8"/>
      <circle cx="36" cy="44" r="24" fill="#1e9be9"/>
      <circle cx="36" cy="54" r="12" fill="#8cd0f6"/>
      <circle cx="36" cy="57" r="7" fill="#fff"/>
      <g font-family="Open Sans,Arial,sans-serif" font-size="5" fill="#fff" text-anchor="middle"><text x="36" y="11">$150M</text><text x="36" y="28">$87M</text><text x="36" y="59" fill="#8cc7f0">$3M</text></g>
    </svg>
    <div class="foot">Tarn Ridge Partners</div><div class="pg">18</div>
  </section>

  <!-- 17 Centered text with progress -->
  <section class="slide">
    <div class="kicker" style="left:148px;top:19px">Subtitle text</div>
    <div class="title" style="left:148px;top:24px">Demo slide<br>With text</div>
    <p class="body abs" style="left:148px;top:58px;width:84px">A short paragraph about the firm and its approach. We partner with owners who seek a clear path to exit and give investors access to one well chosen business.</p>
    <div class="bar-lbl" style="left:148px;top:91px"><span>Step 1</span><span>41%</span></div>
    <div class="abs" style="left:148px;top:95px;width:82px;height:1.2px;background:var(--track)"></div>
    <div class="bar" style="left:148px;top:95px;width:34px"></div>
    <div class="bar-lbl" style="left:148px;top:107px"><span>Step 2</span><span>94%</span></div>
    <div class="abs" style="left:148px;top:111px;width:82px;height:1.2px;background:var(--track)"></div>
    <div class="bar" style="left:148px;top:111px;width:77px"></div>
  </section>

  <!-- 18 Step by step -->
  <section class="slide">
    <div class="title" style="left:18px;top:16px">Demo slide<br>Step by step</div>
    <svg class="abs" style="left:0;top:0" width="258" height="144" viewBox="0 0 258 144">
      <g stroke="#1e9be9" stroke-width="1.6">
        <line x1="0" y1="110" x2="48" y2="110"/><line x1="38" y1="104" x2="104" y2="104"/><line x1="96" y1="98" x2="158" y2="98"/><line x1="150" y1="92" x2="218" y2="92"/><line x1="210" y1="86" x2="258" y2="86"/>
      </g>
    </svg>
    <div class="step" style="left:38px;top:68px"><div class="lbl">Text about step</div><p class="body">Short line for<br>this step here</p><span class="tag">2019</span></div>
    <div class="step" style="left:96px;top:62px"><div class="lbl">Text about step</div><p class="body">Short line for<br>this step here</p><span class="tag">2020</span></div>
    <div class="step" style="left:150px;top:56px"><div class="lbl">Text about step</div><p class="body">Short line for<br>this step here</p><span class="tag">2021</span></div>
    <div class="step" style="left:210px;top:50px"><div class="lbl">Text about step</div><p class="body">Short line for<br>this step here</p><span class="tag">2022</span></div>
    <div class="foot">Tarn Ridge Partners</div><div class="pg">19</div>
  </section>

  <!-- 19 Yearly timeline -->
  <section class="slide">
    <div class="title" style="left:18px;top:16px">Demo slide with<br>Yearly timeline</div>
    <svg class="abs" style="left:0;top:0" width="258" height="144" viewBox="0 0 258 144">
      <line x1="20" y1="104" x2="240" y2="104" stroke="#1e9be9" stroke-width=".8"/>
      <g fill="#1e9be9"><circle cx="20" cy="104" r="2"/><circle cx="81" cy="104" r="2"/><circle cx="142" cy="104" r="2"/></g>
      <circle cx="203" cy="104" r="2" fill="#fff" stroke="#1e9be9" stroke-width=".8"/>
      <g stroke="#9fd0f3" stroke-width=".4" stroke-dasharray="1 1"><line x1="20" y1="64" x2="20" y2="102"/><line x1="81" y1="64" x2="81" y2="102"/><line x1="142" y1="64" x2="142" y2="102"/><line x1="203" y1="64" x2="203" y2="102"/></g>
    </svg>
    <div class="step" style="left:24px;top:62px"><span class="tag">2019</span><div class="lbl" style="color:var(--blue-light)">Text about step</div><p class="body">Short line for<br>this step here</p></div>
    <div class="step" style="left:85px;top:62px"><span class="tag">2020</span><div class="lbl" style="color:var(--blue-light)">Text about step</div><p class="body">Short line for<br>this step here</p></div>
    <div class="step" style="left:146px;top:62px"><span class="tag">2021</span><div class="lbl" style="color:var(--blue-light)">Text about step</div><p class="body">Short line for<br>this step here</p></div>
    <div class="step" style="left:207px;top:62px"><span class="tag">2022</span><div class="lbl" style="color:var(--blue-light)">Text about step</div><p class="body">Short line for<br>this step here</p></div>
    <div class="foot">Tarn Ridge Partners</div><div class="pg">21</div>
  </section>

  <!-- 20 SWOT -->
  <section class="slide">
    <svg class="abs" style="left:0;top:0" width="258" height="144" viewBox="0 0 258 144">
      <g stroke="#e6e6e6" stroke-width="13" stroke-linecap="round"><line x1="94" y1="30" x2="164" y2="112"/><line x1="164" y1="30" x2="94" y2="112"/></g>
      <g fill="#fff" stroke="#dcdcdc" stroke-width=".6"><circle cx="94" cy="30" r="6"/><circle cx="164" cy="30" r="6"/><circle cx="94" cy="112" r="6"/><circle cx="164" cy="112" r="6"/></g>
      <circle cx="94" cy="30" r="4" fill="#4aa8e6"/><circle cx="164" cy="30" r="4" fill="#8cc7f0"/><circle cx="94" cy="112" r="4" fill="#1e9be9"/><circle cx="164" cy="112" r="4" fill="#1470c8"/>
      <g font-family="Open Sans,Arial,sans-serif" font-size="2.6" fill="#8aa"><text x="108" y="46" transform="rotate(50 108 46)">Strength</text><text x="142" y="40" transform="rotate(-50 142 40)">Weakness</text><text x="102" y="100" transform="rotate(-50 102 100)">Threats</text><text x="146" y="90" transform="rotate(50 146 90)">Opportunity</text></g>
      <text x="129" y="74" font-family="Open Sans,Arial,sans-serif" font-size="6" fill="#8cc7f0" text-anchor="middle">SWOT</text>
      <text x="129" y="78" font-family="Open Sans,Arial,sans-serif" font-size="2" fill="#bbb" text-anchor="middle">ANALYSIS</text>
    </svg>
    <div class="item" style="left:20px;top:40px;width:66px;text-align:right"><div class="lbl" style="color:var(--blue-light)">Strength</div><p class="body">Brief line on our key<br>strengths and the edge<br>they give us.</p></div>
    <div class="item" style="left:188px;top:40px;width:66px"><div class="lbl" style="color:var(--blue-light)">Weakness</div><p class="body">Brief line on areas<br>we watch and how we<br>plan to improve.</p></div>
    <div class="item" style="left:20px;top:86px;width:66px;text-align:right"><div class="lbl" style="color:var(--blue-light)">Threats</div><p class="body">Brief line on outside<br>risks and how we<br>guard against them.</p></div>
    <div class="item" style="left:188px;top:86px;width:66px"><div class="lbl" style="color:var(--blue-light)">Opportunity</div><p class="body">Brief line on growth<br>paths we see in the<br>market ahead.</p></div>
    <div class="foot">Tarn Ridge Partners</div>
  </section>

  <!-- 21 Donut chart -->
  <section class="slide">
    <svg class="abs" style="left:20px;top:22px" width="84" height="84" viewBox="0 0 84 84">
      <circle cx="42" cy="42" r="36" fill="none" stroke="#e6e6e6" stroke-width="7"/>
      <circle cx="42" cy="42" r="36" fill="none" stroke="#4aa8e6" stroke-width="4" stroke-dasharray="140 226" transform="rotate(-90 42 42)"/>
      <circle cx="42" cy="42" r="36" fill="none" stroke="#1470c8" stroke-width="4" stroke-dasharray="22 226" stroke-dashoffset="-140" transform="rotate(-90 42 42)"/>
      <text x="42" y="45" font-family="Open Sans,Arial,sans-serif" font-size="9" font-weight="300" fill="#333" text-anchor="middle">2019</text>
      <text x="42" y="52" font-family="Open Sans,Arial,sans-serif" font-size="3" fill="#8cc7f0" text-anchor="middle">Project Name</text>
    </svg>
    <div class="kicker" style="left:136px;top:22px">Subtitle text</div>
    <div class="title" style="left:136px;top:27px">Demo slide<br>With text</div>
    <p class="body abs" style="left:136px;top:60px;width:100px">A short paragraph about the firm and its approach. We partner with owners who seek a clear exit and give investors access to one strong business.</p>
    <svg class="abs" style="left:136px;top:82px" width="100" height="24" viewBox="0 0 100 24">
      <g><circle cx="6" cy="8" r="6" fill="#e6e6e6"/><path d="M6 8V2A6 6 0 1 1 0.5 10z" fill="#4aa8e6"/></g>
      <g><circle cx="30" cy="8" r="6" fill="#e6e6e6"/><path d="M30 8V2A6 6 0 0 1 30 14z" fill="#8cc7f0"/></g>
      <g><circle cx="54" cy="8" r="6" fill="#e6e6e6"/><path d="M54 8V2A6 6 0 0 1 59.6 10z" fill="#4aa8e6"/></g>
      <g><circle cx="78" cy="8" r="6" fill="#e6e6e6"/><path d="M78 8V2A6 6 0 0 1 78 14z" fill="#1470c8"/></g>
      <g font-family="Open Sans,Arial,sans-serif" font-size="2.6" fill="#555" text-anchor="middle"><text x="6" y="20">January</text><text x="30" y="20">February</text><text x="54" y="20">March</text><text x="78" y="20">April</text></g>
    </svg>
    <div class="foot">Tarn Ridge Partners</div><div class="pg">24</div>
  </section>

</main>
</body>
</html>
```